Filmproduktion braucht Visitenkarten und Briefpapier
Zielgruppe
Wir sind eine junge Filmproduktion Firma mit dem Namen Lichtkante.
Unser Kerngeschäft sind Image und Unternehmensfilme, sowie Event und Messefilme.
Aufgabenstellung
Wir sind junge, kreative, Filmschaffende und das soll sich auch in der Visitenkarte widerspiegeln, dennoch macht bitte auch ein paar klassische Vorschläge, manchmal ist weniger mehr.
Unser altes Briefpapier ist angehängt. Das neue Briefpapier muss von uns veränderbar sein, da wir noch nicht alle Daten haben wie Steuernummer und USt-ID, bitte aber schon als Dummy anlegen.
Unsere alten Visitenkarten sind angehängt, diese Daten Stimmen, aber ansonsten stimmt daran nix, wie wir finden. Bitte nicht daran Orientieren!!!
Bitte bei der Adresse Lichtkante GbR schreiben.
Unser neues Logo, jetzt in blau ist ebenfalls angehängt.
Viel Spass beim Designen.

```html
<!DOCTYPE html>
<html lang="de">
<head>
<meta charset="utf-8">
<title>Lichtkante – Geschäftsausstattung</title>
<link href="https://fonts.googleapis.com/css2?family=Source+Sans+3:wght@400;600;700&display=swap" rel="stylesheet">
<style>
  :root {
    --bg: #d6d6d6;
    --paper: #ffffff;
    --folder: #ebebeb;
    --ink: #111111;
    --text: #222222;
    --muted: #555555;
    --blue: #3f8fd2;
    --faint: #efefef;
  }
  * { box-sizing: border-box; margin: 0; padding: 0; }
  html, body { width: 1200px; height: 912px; overflow: hidden; }
  body {
    position: relative;
    background: var(--bg);
    font-family: "Source Sans 3", "Myriad Pro", sans-serif;
    color: var(--text);
  }
  .sheet { position: absolute; overflow: hidden; }
  .folder { left: 17px; top: 124px; width: 340px; height: 577px; background: var(--folder); }
  .letter { background: var(--paper); }
  .letter--main { left: 334px; top: 95px; width: 449px; height: 630px; z-index: 2; }
  .letter--second { left: 783px; top: 136px; width: 400px; height: 577px; z-index: 1; }
  .abs { position: absolute; }

  /* wordmark */
  .wordmark { position: absolute; display: flex; flex-direction: column; align-items: center; }
  .wordmark__dot { border-radius: 50%; background: var(--blue); }
  .wordmark__name { color: var(--ink); font-weight: 400; text-transform: uppercase; white-space: nowrap; }

  /* letter parts */
  .sender-line { font-size: 6px; color: var(--ink); white-space: nowrap; }
  .sender-line .sep { color: var(--blue); }
  .recipient { color: var(--ink); }
  .subject { font-weight: 700; color: var(--ink); white-space: nowrap; }
  .body-text p { margin-bottom: 10.9px; }
  .body-text { color: var(--ink); }
  .sidebar { color: var(--muted); }
  .sidebar h4 { color: var(--blue); font-weight: 700; font-size: inherit; }
  .sidebar .group { margin-bottom: 1em; }
  .sidebar .row { display: flex; }
  .sidebar .row span:first-child { width: 2.8em; }
  .bullet::before { content: "▶"; color: var(--blue); font-size: .8em; margin-right: .7em; }
  .date { font-weight: 700; color: var(--ink); }
  .date .city { color: var(--blue); }
  .backdrop-disc { position: absolute; border-radius: 50%; background: var(--faint); }

  /* business cards */
  .card { position: absolute; top: 725px; height: 141px; background: var(--paper); overflow: hidden; z-index: 3; }
  .card__disc { position: absolute; left: -50px; top: 12px; width: 116px; height: 116px; border-radius: 50%; background: var(--blue); }
  .card__name { position: absolute; left: 85px; top: 20px; font-size: 11.5px; font-weight: 700; color: var(--blue); white-space: nowrap; }
  .card__address { position: absolute; left: 85px; top: 55px; font-size: 7.5px; line-height: 9.8px; color: var(--ink); white-space: nowrap; }
  .card__address .sep { color: var(--blue); }
  .card__contact { position: absolute; left: 85px; top: 94px; font-size: 7.5px; line-height: 9.8px; color: var(--ink); white-space: nowrap; }
  .card--back { background: var(--folder); }
</style>
</head>
<body>

  <!-- Mappe -->
  <section class="sheet folder">
    <div class="wordmark" style="left:0; width:340px; top:225px;">
      <div class="wordmark__dot" style="width:78px;height:78px;margin-bottom:32px;"></div>
      <div class="wordmark__name" style="font-size:20px;letter-spacing:.75em;">Lichtkante</div>
    </div>
  </section>

  <!-- Briefbogen -->
  <section class="sheet letter letter--main">
    <div class="backdrop-disc" style="left:-60px; top:500px; width:290px; height:290px;"></div>

    <p class="abs sender-line" style="left:67px; top:57px;">Lichtkante GbR <span class="sep">|</span> Lindenhof 14 <span class="sep">|</span> 10115 Berlin</p>
    <p class="abs recipient" style="left:64px; top:70px; font-size:8.5px; line-height:11px;">Lichtkante GbR<br>Filmproduktion<br>Lindenhof 14<br>10115 Berlin</p>

    <div class="wordmark" style="left:280px; width:140px; top:58px;">
      <div class="wordmark__dot" style="width:42px;height:42px;margin-bottom:14px;"></div>
      <div class="wordmark__name" style="font-size:10px;letter-spacing:.75em;">Lichtkante</div>
    </div>

    <aside class="abs sidebar" style="left:326px; top:138px; font-size:7.8px; line-height:10px;">
      <div class="group"><h4>Lichtkante GbR</h4>Filmproduktion<br>Lindenhof 14<br>10115 Berlin</div>
      <div class="group"><h4>Geschäftsführer:</h4>Jonas Brenner<br>Lukas Albrecht<br>Henrik Vogt</div>
      <div class="group"><h4>Ansprechpartner:</h4>Lukas Albrecht<br><span class="bullet">(0171) 2 84 55 06</span><br><span class="bullet">albrecht@lichtkante.example</span><br><span class="bullet">www.lichtkante.example</span></div>
      <div class="group"><h4>Bankverbindung:</h4>Stadtbank Mitte
        <div class="row"><span>BLZ:</span><span>200 300 40</span></div>
        <div class="row"><span>Kto.:</span><span>456 789 012</span></div>
        <div class="row"><span>St.-Nr.:</span><span>987/654/32100</span></div>
      </div>
    </aside>

    <h3 class="abs subject" style="left:53px; top:170px; font-size:8.6px;">Filmproduktion braucht Visitenkarten und Briefpapier</h3>

    <div class="abs body-text" style="left:53px; top:191px; width:232px; font-size:8.5px; line-height:10.9px;">
      <p>Wir sind eine junge Filmproduktion Firma mit dem Namen Lichtkante. Unser Kerngeschäft sind Image und Unternehmensfilme, sowie Event und Messefilme.</p>
      <p style="margin-bottom:0;">Wir sind junge, kreative, Filmschaffende und das soll sich auch in der Visitenkarte widerspiegeln, dennoch macht bitte auch ein paar klassische Vorschläge, manchmal ist weniger mehr. Unser altes Briefpapier ist angehängt. Das neue Briefpapier muss von uns veränderbar sein, da wir noch nicht alle Daten haben wie Steuernummer und USt-ID, bitte aber schon als Dummy anlegen.</p>
      <p>Unsere alten Visitenkarten sind angehängt, diese Daten Stimmen, aber ansonsten stimmt daran nix, wie wir finden. Bitte nicht daran Orientieren!!! Bitte bei der Adresse Lichtkante GbR schreiben. Unser neues Logo, jetzt in blau ist ebenfalls angehängt. Viel Spass beim Designen.</p>
      <p>Mit freundlichen Grüßen</p>
      <p>Jansen</p>
    </div>

    <p class="abs date" style="left:53px; top:573px; font-size:8.6px;"><span class="city">Dresden</span>, 17. Oktober 2013</p>
  </section>

  <!-- Briefbogen, zweite Seite -->
  <section class="sheet letter letter--second">
    <div class="backdrop-disc" style="left:-40px; top:460px; width:270px; height:270px;"></div>

    <p class="abs sender-line" style="left:52px; top:52px; font-size:5.5px;">Lichtkante GbR <span class="sep">|</span> Lindenhof 14 <span class="sep">|</span> 10115 Berlin</p>
    <p class="abs recipient" style="left:50px; top:63px; font-size:7.5px; line-height:10px;">Lichtkante GbR<br>Filmproduktion<br>Lindenhof 14<br>10115 Berlin</p>

    <div class="wordmark" style="left:240px; width:135px; top:56px;">
      <div class="wordmark__dot" style="width:36px;height:36px;margin-bottom:14px;"></div>
      <div class="wordmark__name" style="font-size:9px;letter-spacing:.75em;">Lichtkante</div>
    </div>

    <aside class="abs sidebar" style="left:287px; top:126px; font-size:6.9px; line-height:9px;">
      <div class="group"><h4>Lichtkante GbR</h4>Filmproduktion<br>Lindenhof 14<br>10115 Berlin</div>
      <div class="group"><h4>Geschäftsführer:</h4>Jonas Brenner<br>Lukas Albrecht<br>Henrik Vogt</div>
      <div class="group"><h4>Ansprechpartner:</h4>Lukas Albrecht<br><span class="bullet">(0171) 2 84 55 06</span><br><span class="bullet">albrecht@lichtkante.example</span><br><span class="bullet">www.lichtkante.example</span></div>
      <div class="group"><h4>Bankverbindung:</h4>Stadtbank Mitte
        <div class="row"><span>BLZ:</span><span>200 300 40</span></div>
        <div class="row"><span>Kto.:</span><span>456 789 012</span></div>
        <div class="row"><span>St.-Nr.:</span><span>987/654/32100</span></div>
      </div>
    </aside>

    <h3 class="abs subject" style="left:40px; top:154px; font-size:7.6px;">Filmproduktion braucht Visitenkarten und Briefpapier</h3>
    <p class="abs date" style="left:40px; top:521px; font-size:7.6px;"><span class="city">Dresden</span>, 17. Oktober 2013</p>
  </section>

  <!-- Visitenkarten -->
  <article class="card" style="left:174px; width:218px;">
    <div class="card__disc"></div>
    <h2 class="card__name">Lukas Albrecht</h2>
    <p class="card__address">Lichtkante GbR <span class="sep">|</span> Filmproduktion<br>Lindenhof 14<br>10115 Berlin</p>
    <p class="card__contact"><span class="bullet">(0171) 2 84 55 06</span><br><span class="bullet">albrecht@lichtkante.example</span><br><span class="bullet">www.lichtkante.example</span></p>
  </article>

  <article class="card" style="left:392px; width:204px;">
    <div class="card__disc"></div>
    <h2 class="card__name">Henrik Vogt</h2>
    <p class="card__address">Lichtkante GbR <span class="sep">|</span> Filmproduktion<br>Lindenhof 14<br>10115 Berlin</p>
    <p class="card__contact"><span class="bullet">(0160) 73 41 28 95</span><br><span class="bullet">vogt@lichtkante.example</span><br><span class="bullet">www.lichtkante.example</span></p>
  </article>

  <article class="card" style="left:596px; width:205px;">
    <div class="card__disc"></div>
    <h2 class="card__name">Jonas Brenner</h2>
    <p class="card__address">Lichtkante GbR <span class="sep">|</span> Filmproduktion<br>Lindenhof 14<br>10115 Berlin</p>
    <p class="card__contact"><span class="bullet">(0171) 2 84 55 06</span><br><span class="bullet">albrecht@lichtkante.example</span><br><span class="bullet">www.lichtkante.example</span></p>
  </article>

  <article class="card card--back" style="left:801px; width:205px;">
    <div class="wordmark" style="left:0; width:205px; top:28px;">
      <div class="wordmark__dot" style="width:50px;height:50px;margin-bottom:22px;"></div>
      <div class="wordmark__name" style="font-size:11px;letter-spacing:.75em;padding-left:.75em;">Lichtkante</div>
    </div>
  </article>

</body>
</html>
```